Flyer for an anniversary promotion

2nd year anniversary promotion flyer for Quarrywind Dental (logo attached)
Size A4
Promotion runs from Now until 31st Dec 2024
Leave room for actual promotional text which will be in multiple languages (~50 words)
Brand associations
Modern, classy, high quality service, customer care

NOTE - Company SELLS to dental clinics but Quarrywind is a dental products company, not dentists/dental clinics/etc.

Plentimarch wants this to be 300+ words

Target Market(s)

Dental clinics

Industry/Entity Type

Dental

Requirements
Should not have
• Don't use images of teeth

```html
<!DOCTYPE html>
<html lang="en">
<head>
<meta charset="utf-8">
<title>Quarrywind Dental – 2nd Year Anniversary Flyer</title>
<link rel="stylesheet" href="https://fonts.googleapis.com/css2?family=Cinzel:wght@600&family=Montserrat:wght@400;600&display=swap">
<style>
  :root {
    --backdrop: #b0afb0;
    --paper: #f2f2f3;
    --brand-blue: #1e88c6;
    --sky-blue: #3d9bd0;
    --deep-navy: #1e3d5c;
    --ink: #061726;
    --accent-line: #3a95cf;
  }
  * { margin: 0; padding: 0; box-sizing: border-box; }
  html, body {
    width: 1200px; height: 1200px; overflow: hidden;
    background: var(--backdrop);
  }
  .flyer {
    position: absolute;
    left: 215px; top: 60px;
    width: 770px; height: 1080px;
    box-shadow: 0 4px 14px rgba(0,0,0,.25);
  }
  .flyer svg { display: block; width: 100%; height: 100%; }
  .brand-name { font-family: "Cinzel", serif; font-weight: 600; fill: var(--ink); }
  .kicker { font-family: "Montserrat", sans-serif; font-weight: 400; fill: var(--accent-line); letter-spacing: 6px; }
  .headline { font-family: "Cinzel", serif; font-weight: 600; fill: var(--ink); }
  .promo-dates { font-family: "Montserrat", sans-serif; font-weight: 600; fill: var(--accent-line); }
</style>
</head>
<body>
  <div class="flyer">
    <svg viewBox="0 0 1227 1720" xmlns="http://www.w3.org/2000/svg">
      <defs>
        <radialGradient id="sparkle-bg" cx="50%" cy="60%" r="75%">
          <stop offset="0" stop-color="#f6f6f7"/>
          <stop offset="0.6" stop-color="#ececee"/>
          <stop offset="1" stop-color="#e4e4e6"/>
        </radialGradient>
        <radialGradient id="corner-top" cx="100%" cy="0%" r="85%">
          <stop offset="0" stop-color="var(--deep-navy)"/>
          <stop offset="0.45" stop-color="var(--brand-blue)"/>
          <stop offset="1" stop-color="var(--sky-blue)" stop-opacity="0"/>
        </radialGradient>
        <radialGradient id="corner-bottom" cx="0%" cy="100%" r="85%">
          <stop offset="0" stop-color="var(--ink)"/>
          <stop offset="0.45" stop-color="var(--brand-blue)"/>
          <stop offset="1" stop-color="var(--sky-blue)" stop-opacity="0"/>
        </radialGradient>
      </defs>

      <rect class="paper" width="1227" height="1720" fill="var(--paper)"/>
      <rect class="sparkle-backdrop" width="1227" height="1720" fill="url(#sparkle-bg)"
            role="img" aria-label="Soft silver bokeh light background"/>

      <rect class="corner-decor-top" x="0" y="0" width="1227" height="280" fill="url(#corner-top)"
            role="img" aria-label="Decorative blue and navy corner artwork"/>
      <rect class="corner-decor-bottom" x="0" y="1100" width="700" height="620" fill="url(#corner-bottom)"
            role="img" aria-label="Decorative blue and navy corner artwork"/>

      <g class="brand-lockup">
        <rect x="578" y="300" width="70" height="70" fill="var(--brand-blue)"/>
        <text class="brand-name" x="613" y="495" font-size="62" text-anchor="middle">QUARRYWIND</text>
        <text class="brand-name" x="613" y="538" font-size="34" text-anchor="middle" letter-spacing="8">DENTAL</text>
      </g>

      <text class="kicker" x="613" y="658" font-size="32" text-anchor="middle">Celebrating</text>
      <text class="headline" x="613" y="765" font-size="84" text-anchor="middle"
            textLength="1095" lengthAdjust="spacingAndGlyphs">2ND YEAR ANNIVERSARY</text>

      <g class="promo-period">
        <rect x="178" y="804" width="866" height="3" fill="var(--accent-line)"/>
        <text class="promo-dates" x="611" y="849" font-size="32" text-anchor="middle">Promotion runs from Now until 31st Dec 2024</text>
        <rect x="178" y="864" width="866" height="3" fill="var(--accent-line)"/>
      </g>
    </svg>
  </div>
</body>
</html>
```